Business Card Design

- one on one personal training
- group personal training
- indoor or outdoor training available
- fitness and health assessments
- personalised fitness programs
- flexible hours for training

I am a Personal Trainer in Perth Australia. I am looking to expand my word of mouth client base.

I would like to see something that uses the colours blue, green and/or yellow.

The final design should reflect the way that I train clients, fun, motivating and perhaps a little quirky?
Updates

update with a logo with the letters MPT thank you

Hi all, Have had some great designs so far. Have decided to go double sided, perhaps to use the back to list my services. Thank you

Please check update brief. Thank you.

Target Market(s)

Professionals, ages 30 to 60

Industry/Entity Type

Training

Contact Information for Business Card

Mira Ostrowski
Personal Trainer

0491 570 118
mirapersonaltrainer@quillnest.com
http://www.mirapersonaltrainer.net

Requirements
Must have
• A logo with the letter MPT
Nice to have
• a logo to represent either; fitness, health, change, overall well-being.
Should not have
• Please no weights or lotus flowers!!

```html
<!DOCTYPE html>
<html lang="en">
<head>
<meta charset="utf-8">
<title>MPT Business Card – Mira Ostrowski</title>
<link rel="stylesheet" href="https://fonts.googleapis.com/css2?family=Source+Sans+3:ital,wght@0,400;0,600;1,400&display=swap">
<style>
  :root {
    --card-black: #000000;
    --accent-yellow: #fdb813;
    --text-white: #ffffff;
    --photo-dark: #1a1a1a;
    --photo-mid: #3a3a3a;
    --text-font: "Source Sans 3", "Myriad Pro", Arial, sans-serif;
  }
  html, body {
    margin: 0;
    padding: 0;
    width: 1200px;
    height: 741px;
    overflow: hidden;
    background: var(--card-black);
  }
  .card {
    position: relative;
    width: 1200px;
    height: 741px;
    background: var(--card-black);
    font-family: var(--text-font);
    color: var(--text-white);
    overflow: hidden;
  }
  .side-band {
    position: absolute;
    left: 0; top: 0;
    width: 61px; height: 741px;
    background: var(--accent-yellow);
  }
  .brand {
    position: absolute;
    left: 101px; top: 110px;
    display: flex;
    align-items: center;
    gap: 22px;
    height: 72px;
  }
  .brand-mark {
    width: 56px; height: 56px;
    background: var(--accent-yellow);
  }
  .brand-name {
    margin: 0;
    font-size: 66px;
    font-weight: 400;
    line-height: 1;
    color: var(--text-white);
  }
  .trainer-name {
    position: absolute;
    right: 63px; top: 84px;
    margin: 0;
    font-size: 45px;
    font-weight: 600;
    font-variant: small-caps;
    line-height: 1;
    color: var(--accent-yellow);
  }
  .trainer-role {
    position: absolute;
    right: 63px; top: 142px;
    margin: 0;
    font-size: 42px;
    font-style: italic;
    font-weight: 400;
    line-height: 1;
    color: var(--text-white);
  }
  .header-rule {
    position: absolute;
    left: 484px; top: 198px;
    width: 676px; height: 3px;
    background: var(--accent-yellow);
  }
  .training-photo {
    position: absolute;
    left: 675px; top: 214px;
    width: 495px; height: 292px;
    background: radial-gradient(ellipse at 45% 50%, var(--photo-mid) 0%, var(--photo-dark) 55%, var(--card-black) 100%);
  }
  .contact {
    position: absolute;
    left: 101px; top: 288px;
    margin: 0;
    font-style: normal;
  }
  .contact-phone {
    display: block;
    font-size: 42px;
    line-height: 50px;
    color: var(--text-white);
  }
  .contact-line {
    display: block;
    font-size: 34px;
    line-height: 51px;
    color: var(--text-white);
  }
  .accent { color: var(--accent-yellow); }
  .services {
    position: absolute;
    left: 95px; top: 522px;
    margin: 0;
    padding: 0;
    list-style: none;
    font-size: 29px;
    line-height: 50px;
    color: var(--accent-yellow);
  }
  .services li { white-space: nowrap; }
  .sep {
    display: inline-block;
    width: 4px; height: 24px;
    margin: 0 14px;
    background: var(--accent-yellow);
    vertical-align: -3px;
  }
  .sep:first-child { margin-left: 0; }
</style>
</head>
<body>
  <main class="card">
    <div class="side-band"></div>

    <div class="brand">
      <div class="brand-mark"></div>
      <h1 class="brand-name">MPT</h1>
    </div>

    <h2 class="trainer-name">Mira Ostrowski</h2>
    <p class="trainer-role">Personal Trainer</p>
    <div class="header-rule"></div>

    <div class="training-photo" role="img" aria-label="Dark photo of a gloved hand lifting a dumbbell"></div>

    <address class="contact">
      <span class="contact-phone">0491 570 118</span>
      <span class="contact-line">mirapersonaltrainer<span class="accent">@quillnest.com</span></span>
      <span class="contact-line">www.<span class="accent">mirapersonaltrainer</span>.net</span>
    </address>

    <ul class="services">
      <li><span class="sep"></span>one on one personal training<span class="sep"></span>indoor or outdoor training available<span class="sep"></span></li>
      <li><span class="sep"></span>group personal training<span class="sep"></span>fitness and health assessments<span class="sep"></span></li>
      <li><span class="sep"></span>personalised fitness programs<span class="sep"></span></li>
    </ul>
  </main>
</body>
</html>
```